Business card design for sports medicine and athlete care clinic.

We need a bold, solid business card design for our practitioners to stand out. We treat overuse & sports-related injuries and provide post-operative rehabilitation. Our specialisations include chronic conditions, men’s health, nutrition & musculoskeletal disorders (MSDs). All brand collateral in terms of fonts, logo and colour palette to be provided.

Target Market(s)

Athletes (professional and amateur), sportspeople, predominantly male

Industry/Entity Type

Health And Wellness

Contact Information for Business Card

The front of the card should be white with dark blue text the back dark blue with white text. The logo should be top-left. The business name should be horizontal and right of the logo. The tagline should be directly below centred on the back of the card (see top-banner.png and bottom-banner.png)

Font styles to use
Sans Serif

Colors
0355a3
0293ce
3176b5
ffffff
85acd3

Requirements
Nice to have
• Diagonal and/or horizontal line elements between logo and practitioner details and/or bottom corner of card (see slide.png and tag-bg.png).

```html
<!DOCTYPE html>
<html lang="en">
<head>
<meta charset="utf-8">
<title>The Runner's Lodge – Business Card</title>
<link rel="stylesheet" href="https://fonts.googleapis.com/css2?family=Montserrat:ital,wght@0,400;0,700;0,800;1,400&display=swap">
<style>
  :root {
    --page: #e4e4e4;
    --navy: #0f2a6b;
    --navy-deep: #081a4f;
    --navy-light: #123d7e;
    --ink: #1b2f6e;
    --cyan: #00b4e3;
    --white: #ffffff;
  }
  * { margin: 0; padding: 0; box-sizing: border-box; }
  html, body { width: 1200px; height: 1200px; overflow: hidden; }
  body {
    background: var(--page);
    font-family: "Montserrat", Arial, sans-serif;
    position: relative;
  }
  .card {
    position: absolute;
    left: 262px;
    width: 686px;
    height: 392px;
    border-radius: 26px;
    overflow: hidden;
  }
  .card-front { top: 165px; background: var(--white); }
  .card-back {
    top: 653px;
    background: linear-gradient(135deg, var(--navy-deep) 0%, var(--navy) 55%, var(--navy-light) 100%);
  }
  .wave { position: absolute; left: 0; top: 0; width: 686px; height: 392px; }

  .brand-mark {
    position: absolute; left: 112px; top: 68px;
    width: 70px; height: 70px; border-radius: 50%;
    background: var(--cyan);
  }
  .brand-name {
    position: absolute; left: 201px; top: 70px;
    font-size: 42px; font-weight: 700; color: var(--navy);
    letter-spacing: -0.3px; white-space: nowrap;
  }
  .brand-tagline {
    position: absolute; left: 203px; top: 118px;
    font-size: 18.5px; font-weight: 700; color: var(--cyan);
    white-space: nowrap;
  }

  .person {
    position: absolute; right: 404px; top: 198px; text-align: right;
  }
  .person-name { font-size: 24px; font-weight: 700; color: var(--navy); white-space: nowrap; }
  .person-role { font-size: 16px; font-style: italic; color: var(--ink); margin-top: 1px; }

  .divider {
    position: absolute; left: 305px; top: 171px;
    width: 1px; height: 99px; background: var(--navy);
  }

  .contact { position: absolute; left: 336px; top: 170px; list-style: none; }
  .contact li {
    position: relative; padding-left: 13px;
    font-size: 15.5px; line-height: 19.5px; color: var(--ink);
    white-space: nowrap;
  }
  .contact li + li { margin-top: 0; }
  .contact li.gap { margin-top: 6px; }
  .contact svg { position: absolute; left: -2px; top: 4px; width: 12px; height: 12px; fill: var(--navy); }

  .social {
    position: absolute; right: 45px; top: 351px;
    display: flex; align-items: center; gap: 6px;
    color: var(--white); font-size: 15.5px;
  }
  .social-dot { width: 13px; height: 13px; border-radius: 50%; background: var(--white); }

  .back-mark {
    position: absolute; left: 283px; top: 70px;
    width: 120px; height: 120px; border-radius: 50%;
    background: var(--cyan);
  }
  .back-name {
    position: absolute; left: 0; right: 0; top: 210px; text-align: center;
    font-size: 30px; font-weight: 700; color: var(--white);
  }
  .back-tagline {
    position: absolute; left: 0; right: 0; top: 330px; text-align: center;
    font-size: 15.5px; color: var(--white);
  }
</style>
</head>
<body>

<section class="card card-front">
  <div class="brand-mark"></div>
  <h1 class="brand-name">The Runner’s Lodge</h1>
  <p class="brand-tagline">Sports medicine and athlete care</p>

  <div class="person">
    <p class="person-name">Daniel Hart</p>
    <p class="person-role">President</p>
  </div>

  <div class="divider"></div>

  <ul class="contact">
    <li>
      <svg viewBox="0 0 12 12"><path d="M6 0C3.8 0 2 1.8 2 4c0 3 4 8 4 8s4-5 4-8c0-2.2-1.8-4-4-4zm0 5.6A1.6 1.6 0 1 1 6 2.4a1.6 1.6 0 0 1 0 3.2z"/></svg>
      4120 Harbor View Road<br>Juneau, Alaska 34812
    </li>
    <li class="gap">
      <svg viewBox="0 0 12 12"><path d="M2.4 0.5l2 .3 1 2.6-1.3 1a7 7 0 0 0 3.5 3.5l1-1.3 2.6 1 .3 2c0 .8-.7 1.4-1.5 1.4C4.8 11 1 7.2 1 2c0-.8.6-1.5 1.4-1.5z"/></svg>
      482-310-7754
    </li>
    <li>
      <svg viewBox="0 0 12 12"><path d="M1 3h10v6H1z M1.5 3.5L6 6.8l4.5-3.3" stroke="#fff" stroke-width="0.9"/></svg>
      info@therunnerslodge.com.au
    </li>
    <li>
      <svg viewBox="0 0 12 12"><circle cx="6" cy="6" r="5.2"/><path d="M3 4.5c1 .4 1.4 1.4 2.4 1.6.6.8-.2 2 .5 3M7.6 2.4c-.3 1 .6 1.5 1.6 1.6.5.5.4 1.5 1 1.8" stroke="#fff" stroke-width="0.9" fill="none"/></svg>
      therunnerslodge.com.au
    </li>
  </ul>

  <svg class="wave" viewBox="0 0 686 392" aria-hidden="true">
    <path fill="var(--cyan)" d="M0,316 C100,362 210,370 330,358 C440,346 510,298 600,298 C640,298 665,322 686,338 L686,392 L0,392 Z"/>
    <path fill="var(--white)" d="M0,317 C100,363 210,372 330,362 C440,352 515,310 600,306 C640,304 665,326 686,342 L686,392 L0,392 Z"/>
    <path fill="var(--navy)" d="M0,318 C90,362 200,374 330,367 C440,360 520,322 600,314 C640,310 665,332 686,347 L686,392 L0,392 Z"/>
  </svg>

  <div class="social">
    <span class="social-dot"></span>
    <span>RunnersLodgeAU</span>
  </div>
</section>

<section class="card card-back">
  <div class="back-mark"></div>
  <p class="back-name">The Runner’s Lodge</p>
  <p class="back-tagline">Delivering excellence in sports medicine &amp; athlete care</p>
</section>

</body>
</html>
```